Product Image Design: Claiming the Salary You Deserve at Last (Plus Bonus!)

I need a product image designed for a new product I will be selling on sellvantrix.com that teaches how to quickly make more money by getting a raise or promotion.

Dimensions must be 1280 x 720 pixels. The product title and subtitle are as follows:

Title: Claiming the Full Salary You Deserve at Last (Plus Bonus!)

Subtitle: The Quickest Route toward a Huge Pay Bump Minus Costly Schooling Plus Flattering of Management

I'm looking for a design that is eye catching and communicates the idea of business success and getting paid more money from a company or employer.

The target audience is professional men in their 20s and 30s who are looking to quickly make more money and advance in their careers.

Target Market(s)

Professional men in their 20s and 30s who are looking to quickly make more money and advance in their careers.

Industry/Entity Type

Professional Service

Font styles to use
Serif

Requirements
Must have
• Title and subtitle provided in project description.

Final design in 1280 x 720 dimensions (or larger with same width to height ratio).

Eye catching font, colors and graphics, but not overly flashy.

Masculine colors (i.e. no pinks or other feminine colors).
Nice to have
• N/A
Should not have
• Feminine colors or images of women.

```html
<!DOCTYPE html>
<html lang="en">
<head>
<meta charset="utf-8">
<title>Claiming the Full Salary You Deserve at Last (Plus Bonus!)</title>
<link rel="stylesheet" href="https://fonts.googleapis.com/css2?family=Anton&family=Roboto+Condensed:wght@400;700;900&display=swap">
<style>
  :root {
    --page: #ffffff;
    --blue: #2a5fae;
    --blue-deep: #1f4f9c;
    --blue-light: #3a74c4;
    --yellow: #f8cf1c;
    --yellow-deep: #f2bf12;
    --khaki: #cdb894;
    --denim: #9cbbe2;
    --sneaker: #f2f2f2;
    --ink: #1b1b1b;
    --white: #ffffff;
  }
  html, body {
    margin: 0;
    padding: 0;
    width: 1200px;
    height: 926px;
    overflow: hidden;
    background: var(--page);
  }
  .canvas {
    position: relative;
    width: 1200px;
    height: 926px;
  }
  .banner {
    position: absolute;
    left: 159px;
    top: 187px;
    width: 901px;
    height: 506px;
    overflow: hidden;
    background: radial-gradient(ellipse at 40% 45%, var(--blue-light) 0%, var(--blue) 55%, var(--blue-deep) 100%);
    font-family: "Anton", "Impact", sans-serif;
  }

  /* photo area: man with laptop, money and yellow splash */
  .hero-photo {
    position: absolute;
    left: 445px;
    top: 20px;
    width: 440px;
    height: 440px;
  }
  .hero-splash {
    position: absolute;
    left: 40px;
    top: 90px;
    width: 350px;
    height: 250px;
    border-radius: 48% 52% 44% 56% / 50% 46% 54% 50%;
    background: linear-gradient(135deg, var(--yellow) 0%, var(--yellow-deep) 100%);
    transform: rotate(-14deg);
  }
  .hero-figure {
    position: absolute;
    left: 110px;
    top: 50px;
    width: 220px;
    height: 340px;
    border-radius: 110px 110px 40px 40px;
    background: linear-gradient(180deg, #c89a78 0%, var(--khaki) 30%, var(--khaki) 55%, var(--denim) 70%, #86a9d6 100%);
  }
  .hero-shoes {
    position: absolute;
    left: 95px;
    top: 368px;
    width: 250px;
    height: 34px;
    border-radius: 16px;
    background: var(--sneaker);
  }
  .hero-shadow {
    position: absolute;
    left: 70px;
    top: 392px;
    width: 300px;
    height: 34px;
    border-radius: 50%;
    background: rgba(15, 40, 85, 0.45);
  }
  .hero-money {
    position: absolute;
    border-radius: 4px;
  }
  .hero-money.bill { background: #9fb08f; }
  .hero-money.coin { background: #e8b21c; border-radius: 50%; }

  .headline-tag {
    position: absolute;
    left: 141px;
    top: 98px;
    height: 45px;
    padding: 0 12px;
    background: var(--yellow);
    color: var(--ink);
    font-size: 31px;
    line-height: 45px;
    white-space: nowrap;
    text-transform: uppercase;
  }
  .headline-main {
    position: absolute;
    left: 49px;
    top: 146px;
    width: 395px;
    margin: 0;
    color: var(--white);
    font-size: 47px;
    font-weight: 400;
    line-height: 58px;
    text-align: center;
    white-space: nowrap;
    text-transform: uppercase;
  }
  .headline-bar {
    position: absolute;
    left: 37px;
    top: 218px;
    width: 406px;
    height: 80px;
    background: var(--ink);
    color: var(--white);
    font-size: 58px;
    line-height: 80px;
    text-align: center;
    white-space: nowrap;
    text-transform: uppercase;
  }
  .pointer-arrow {
    position: absolute;
    left: 78px;
    top: 300px;
    width: 52px;
    height: 38px;
  }
  .headline-bonus {
    position: absolute;
    left: 138px;
    top: 322px;
    color: var(--white);
    font-size: 36px;
    line-height: 44px;
    white-space: nowrap;
    text-transform: uppercase;
  }
  .speech-bubble {
    position: absolute;
    left: 684px;
    top: 14px;
    width: 200px;
    height: 165px;
  }
  .speech-bubble svg {
    position: absolute;
    inset: 0;
  }
  .bubble-text {
    position: absolute;
    left: 24px;
    top: 40px;
    width: 156px;
    margin: 0;
    transform: rotate(17deg);
    transform-origin: 50% 50%;
    color: var(--white);
    font-family: "Roboto Condensed", "Arial Narrow", sans-serif;
    text-align: center;
  }
  .bubble-lead {
    display: block;
    font-size: 14px;
    font-weight: 900;
    line-height: 15px;
    text-transform: uppercase;
  }
  .bubble-sub {
    display: block;
    font-size: 9.5px;
    font-weight: 700;
    line-height: 11px;
  }
</style>
</head>
<body>
<div class="canvas">
  <section class="banner">
    <div class="hero-photo" role="img" aria-label="Smiling young man sitting cross-legged with a yellow laptop, pointing at the title, in front of a yellow brush splash with flying dollar bills and gold coins">
      <div class="hero-splash"></div>
      <div class="hero-shadow"></div>
      <div class="hero-figure"></div>
      <div class="hero-shoes"></div>
      <div class="hero-money bill" style="left:60px;top:6px;width:80px;height:30px;transform:rotate(-18deg)"></div>
      <div class="hero-money coin" style="left:200px;top:0;width:40px;height:22px"></div>
      <div class="hero-money coin" style="left:120px;top:40px;width:34px;height:18px"></div>
      <div class="hero-money coin" style="left:5px;top:72px;width:30px;height:16px"></div>
      <div class="hero-money coin" style="left:84px;top:94px;width:36px;height:18px"></div>
      <div class="hero-money bill" style="left:0;top:310px;width:80px;height:30px;transform:rotate(58deg)"></div>
      <div class="hero-money bill" style="left:-60px;top:420px;width:96px;height:34px;transform:rotate(28deg)"></div>
      <div class="hero-money bill" style="left:325px;top:175px;width:60px;height:26px;transform:rotate(-40deg)"></div>
      <div class="hero-money coin" style="left:372px;top:168px;width:34px;height:20px"></div>
      <div class="hero-money bill" style="left:325px;top:290px;width:86px;height:34px;transform:rotate(-24deg)"></div>
      <div class="hero-money coin" style="left:310px;top:345px;width:30px;height:30px"></div>
      <div class="hero-money coin" style="left:400px;top:332px;width:28px;height:16px"></div>
    </div>

    <div class="headline-tag">Claiming the Full</div>
    <h1 class="headline-main">Salary You Deserve</h1>
    <div class="headline-bar">At Last</div>

    <svg class="pointer-arrow" viewBox="0 0 52 38" aria-hidden="true">
      <path d="M4 6 L30 22" stroke="#ffffff" stroke-width="3" stroke-dasharray="4 3" fill="none"/>
      <path d="M26 12 L46 30 L22 32 Z" fill="#ffffff"/>
    </svg>

    <div class="headline-bonus">[Plus Bonus!]</div>

    <div class="speech-bubble">
      <svg viewBox="0 0 200 165" aria-hidden="true">
        <path d="M100 12 C160 12 192 48 190 86 C188 124 150 148 100 146 C78 145 60 140 46 132 L14 150 L30 118 C16 104 10 88 12 72 C16 36 50 12 100 12 Z"
              fill="none" stroke="#f8cf1c" stroke-width="4" stroke-linejoin="round"/>
      </svg>
      <p class="bubble-text">
        <span class="bubble-lead">The Quickest Route</span>
        <span class="bubble-sub">toward a Huge Pay Bump Minus Costly Schooling Plus Flattering of Management</span>
      </p>
    </div>
  </section>
</div>
</body>
</html>
```